依頼詳細
◇サイトマップ
①Home
② MENU&PRICE
③ SALON INFO
④ PRODUCTS
⑤ COUPON
⑥ GALLERY
⑦ STAFF
⑧ MOVI
⑨ RECRUIT
⑩ CONTACT
⑪BLOG(一覧)
⑫NEWS(一覧)
⑬アクセサリー

◇優先事項
1.ユーザビリティー
2.デザイン
3.編集更新

◇効果
1.新規顧客の獲得
2.売上の向上
3.認知度向上(情報発信)

◇ターゲット
男性客は多いので、集客は女性をメインにしたい。
30~40代をメインだが、20代の人もターゲットに入る
会社員、自営業など全体的に伸ばしたい。

◇提供素材
ロゴデータなし。
店舗内装に写真はある。
動画もとっているものがある。

◇sns
フェイスブック
ツイッター
ラインアット
をしている。

◇その他アプリ
メール予約のシステムを使っている

◇デザイン
シンプル  3   複雑
単色    4~5 カラフル
暗い    4   明るい
日常    1   高級
遊び心  1~2  厳粛
未来的  1~2  伝統的
女性   1    男性

◇テイスト
モダン・アンティーク・レトロなデザインが好き
フォーマル・幻想的・神秘的・知性的はイメージと違う

◇カラー
ベースは白やクリーム系
サロンの雰囲気に合わせて茶色やその他の差し色

◇参考サイト
特に無いが、情報がしっかり発信出来るサイトがベスト。
サイトURL
http://www.velvora-style.com/
ページ数
1ページ
希望イメージ
シンプル 複雑
単色 カラフル
暗い 明るい
日常 高級
遊び心 厳粛
未来的 伝統的
女性的 男性的
希望する色
茶系、 ベースは白やクリーム系 サロンの雰囲気に合わせて茶色やその他の差し色
納品ファイル
• イラストレーター形式 (.ai)
• フォトショップ形式 (.psd)
• PNG形式 (.png)
補足説明
◇素材
1.現行のサイトに有る写真やテキストは自由に使って頂いて構いません。

2.この度素材として撮影をしているものを、ソラデポットにてダウンロードしてお使い下さい。
http://soradepot.net/download/7b2e41d09a5c8f3e6d1a2b4c9e0f57a8d6c3b1e2
パスワード kiro

3.当店にてピクスナを契約していますのでその中から使用して一旦カンプ画像を入れておいて下さい。
https://jp.pixuna-stock.com/

※その他は商用利用可能な無料のものをお使い下さい。
もう少し提案が見たいため延長させて頂きます。
もう少し提案を頂ければと思います。
何卒宜しくお願い致します。
もう少しデザインを見てみたいため延長させていただきます。
宜しくお願い致します。

ひと目見て気に入りました。

素早い対応ありがとうございました。

```html
<!DOCTYPE html>
<html lang="ja">
<head>
<meta charset="utf-8">
<title>Velvora Hair Make Studio</title>
<link rel="stylesheet" href="https://fonts.googleapis.com/css2?family=Noto+Sans+JP:wght@400;500;700&family=Noto+Serif+JP:wght@500;700&display=swap">
<style>
:root{
  --cream:#f6efe4;
  --cream-dark:#efe4d3;
  --white:#ffffff;
  --brown:#6b3a16;
  --brown-dark:#4a2810;
  --text:#3b2f27;
  --muted:#7a6e64;
  --line:#e0d6c8;
}
*{margin:0;padding:0;box-sizing:border-box}
html,body{width:1200px;height:3220px;overflow:hidden}
body{background:var(--white);font-family:"Noto Sans JP",sans-serif;color:var(--text);position:relative}
.abs{position:absolute}
.hero{left:0;top:0;width:1200px;height:420px;background:linear-gradient(100deg,#c9b79a 0%,#e8dccb 40%,#d8c6ac 70%,#a8927a 100%)}
.brand{left:0;top:150px;width:1200px;text-align:center;font-family:"Noto Serif JP",serif;font-weight:700;color:var(--brown);font-size:44px;letter-spacing:1px}
.brand small{display:block;font-size:15px;letter-spacing:3px;margin-top:2px}
.social{left:0;top:280px;width:1200px;display:flex;justify-content:center;gap:12px}
.social span{width:30px;height:30px;border-radius:50%;background:var(--brown-dark)}
.nav{left:0;top:376px;width:1200px;height:44px;background:rgba(40,25,15,.55);display:flex;justify-content:center;align-items:center;gap:38px}
.nav a{color:var(--white);font-size:13px;text-decoration:none;letter-spacing:1px}
.nav a.current{border-bottom:1px solid var(--white);padding-bottom:2px}
.sec-title{left:0;width:1200px;text-align:center;font-size:20px;letter-spacing:2px;font-weight:500}
.sec-title small{display:block;font-size:11px;color:var(--muted);margin-top:4px}
.concept-band{left:0;top:420px;width:1200px;height:380px;background:var(--cream)}
.concept-lines{left:0;top:608px;width:1200px;text-align:center;font-size:13px;line-height:30px;color:var(--muted)}
.feature{left:0;top:800px;width:1200px;height:410px;background:var(--cream-dark)}
.feature-photo{left:160px;top:838px;width:360px;height:340px;background:linear-gradient(135deg,#d9d2c4,#a89c86 60%,#6f6a55)}
.feature-body{left:520px;top:838px;width:528px;height:340px;background:var(--white);padding:50px 36px}
.feature-body h2{font-family:"Noto Serif JP",serif;font-size:22px;font-weight:700;margin-bottom:26px}
.feature-body p{font-size:12.5px;line-height:25px;color:var(--muted)}
.gallery-photo{top:1368px;width:280px;height:200px}
.btn{height:28px;background:var(--brown);color:var(--white);font-size:11px;letter-spacing:1px;display:flex;align-items:center;justify-content:center}
.news-band{left:0;top:1720px;width:1200px;height:480px;background:var(--cream)}
.news-box{top:1760px;width:440px;height:400px;background:var(--white);padding:30px 40px}
.news-box h3{text-align:center;font-size:20px;font-weight:500;letter-spacing:2px}
.news-box h3 small{display:block;font-size:11px;color:var(--muted);font-weight:400}
.news-box ul{list-style:none;margin-top:40px}
.news-box li{font-size:11.5px;color:var(--muted);height:30px;line-height:30px;border-bottom:1px solid var(--line)}
.news-box li time{margin-right:24px}
.news-box .btn{position:absolute;left:100px;bottom:36px;width:240px}
.tile{top:2260px;width:240px;height:220px;display:flex;align-items:center;justify-content:center;color:var(--white);font-family:"Noto Serif JP",serif;font-size:22px;letter-spacing:2px}
.map{left:0;top:2540px;width:1200px;height:428px;background:linear-gradient(180deg,#dcdcdc,#c9c9c9)}
.footer{left:0;top:2968px;width:1200px;height:212px;background:var(--cream)}
.foot-brand{left:96px;top:3010px;font-family:"Noto Serif JP",serif;font-weight:700;color:var(--brown);font-size:30px}
.foot-brand small{display:block;font-size:11px;letter-spacing:2px}
.foot-info{font-size:11px;line-height:22px;color:var(--muted)}
.copy{left:0;top:3180px;width:1200px;height:40px;background:var(--brown-dark);color:#e8dccb;font-size:10px;text-align:center;line-height:40px}
</style>
</head>
<body>
<header>
  <div class="abs hero" role="img" aria-label="サロン店内の写真（椅子と鏡、暖かい照明）"></div>
  <div class="abs brand">Velvora<small>Hair Make Studio</small></div>
  <div class="abs social"><span></span><span></span><span></span></div>
  <nav class="abs nav">
    <a class="current">HOME</a><a>MENU&amp;PRICE</a><a>SALON INFO</a><a>STAFF</a><a>RECRUIT</a><a>CONTACT</a>
  </nav>
</header>

<section>
  <div class="abs concept-band"></div>
  <h2 class="abs sec-title" style="top:500px">CONCEPT<small>コンセプト</small></h2>
  <div class="abs concept-lines">
    <p>高いカット技術で素敵な毎日をお届けする場所</p>
    <p>ゆったりくつろげる空間</p>
    <p>大切な時間に寄り添うスタイル</p>
    <p>一人ひとりに似合う髪型を提案</p>
    <p>髪質に合わせたトリートメント</p>
  </div>
</section>

<section>
  <div class="abs feature"></div>
  <div class="abs feature-photo" role="img" aria-label="店内の棚と観葉植物の写真"></div>
  <div class="abs feature-body">
    <h2>癒しの場としてのサロン</h2>
    <p>「何気ない日常を少し特別に」そんな思いで、ひとりひとりのお客様と丁寧に向き合っています。<br>
    お仕事や家事の合間に、心も体もほっと休まる時間をご用意しています。<br>
    季節やライフスタイルに合わせて、扱いやすく長持ちするヘアを提案します。<br>
    どうぞお気軽にご来店ください。スタッフ一同お待ちしております。</p>
  </div>
</section>

<section>
  <h2 class="abs sec-title" style="top:1296px">GALLERY</h2>
  <div class="abs gallery-photo" style="left:152px;background:linear-gradient(135deg,#8aa0b8,#c4b8ac)" role="img" aria-label="ヘアスタイル作品の写真"></div>
  <div class="abs gallery-photo" style="left:460px;background:linear-gradient(135deg,#b9c6d0,#8d8f94)" role="img" aria-label="ヘアスタイル作品の写真"></div>
  <div class="abs gallery-photo" style="left:768px;background:linear-gradient(135deg,#aeb4bc,#6c6a68)" role="img" aria-label="ヘアスタイル作品の写真"></div>
  <div class="abs btn" style="left:500px;top:1604px;width:200px">MORE</div>
</section>

<section>
  <div class="abs news-band"></div>
  <div class="abs news-box" style="left:150px">
    <h3>BLOG<small>ブログ</small></h3>
    <ul>
      <li><time>2017.05.20</time>タイトルタイトルタイトルタイトル</li>
      <li><time>2017.05.20</time>タイトルタイトルタイトルタイトル</li>
      <li><time>2017.05.20</time>タイトルタイトルタイトルタイトル</li>
      <li><time>2017.05.20</time>タイトルタイトルタイトルタイトル</li>
      <li><time>2017.05.20</time>タイトルタイトルタイトルタイトル</li>
    </ul>
    <div class="btn">MORE</div>
  </div>
  <div class="abs news-box" style="left:610px">
    <h3>NEWS<small>ニュース</small></h3>
    <ul>
      <li><time>2017.04.01</time>タイトルタイトルタイトルタイトル</li>
      <li><time>2017.04.01</time>タイトルタイトルタイトルタイトル</li>
      <li><time>2017.04.01</time>タイトルタイトルタイトルタイトル</li>
      <li><time>2017.04.01</time>タイトルタイトルタイトルタイトル</li>
      <li><time>2017.04.01</time>タイトルタイトルタイトルタイトル</li>
    </ul>
    <div class="btn">MORE</div>
  </div>
</section>

<section>
  <div class="abs tile" style="left:100px;background:linear-gradient(135deg,#8a6a4c,#4a3322)" role="img" aria-label="クーポン：アンティークの鞄の写真">COUPON</div>
  <div class="abs tile" style="left:352px;background:linear-gradient(135deg,#b8a892,#6e5e4c)" role="img" aria-label="商品：ヘアケア製品の写真">PRODUCT</div>
  <div class="abs tile" style="left:604px;background:linear-gradient(135deg,#7f8a60,#3d4630)" role="img" aria-label="動画：店内の様子の写真">MOVIE</div>
  <div class="abs tile" style="left:856px;background:linear-gradient(135deg,#a89272,#52402c)" role="img" aria-label="求人：ヘアアクセサリーの写真">RECRUIT</div>
</section>

<div class="abs map" role="img" aria-label="サロン周辺の地図"></div>

<footer>
  <div class="abs footer"></div>
  <div class="abs foot-brand">Velvora<small>Hair Make Studio</small></div>
  <div class="abs foot-info" style="left:300px;top:3020px">
    <p>〒552-0001 大阪府北浜市みなと区1-2-3</p>
    <p>最寄り駅より徒歩5分 駐車場あり</p>
  </div>
  <div class="abs btn" style="left:640px;top:3016px;width:200px">&#9742; 06-1234-5678</div>
  <div class="abs btn" style="left:640px;top:3056px;width:200px">&#9993; CONTACT</div>
  <div class="abs foot-info" style="left:880px;top:3016px">
    <p>営業時間 平日 10:00〜20:00</p>
    <p>土日祝 10:00〜18:00</p>
    <p>定休日 毎週月曜日</p>
  </div>
  <div class="abs social" style="top:3130px"><span style="width:22px;height:22px"></span><span style="width:22px;height:22px"></span><span style="width:22px;height:22px"></span></div>
  <div class="abs copy">copyright © Velvora Hair Make Studio All Rights Reserved.</div>
</footer>
</body>
</html>
```